BRISKWAY ELECTRICAL SIGN

We are wanting a sign to mount on the side of the road to attract peoples attention, it will be 1200mm high by 2400mm wide. We want it to stand out from the others, modern sharp looking, We are an electrical contractor who wants to be the market leader and supplier of choice to our current clients and futre clients.

Industry/Entity Type

Electrical

Colors

Designer to choose colors to be used in the design.

Requirements
Must have
• Name: Briskway Electrical
• Our logo as per uploaded files
• The words: Design - Installation - Maintenance
• Freecall: 0800 342 958
• Mobile : 021 736 4192 (delete mobile number if gets to cluttered)
• Web: www.briskway.net.nz
Should not have
• a light bulb, or plug

```html
<!DOCTYPE html>
<html lang="en">
<head>
<meta charset="utf-8">
<title>Briskway Electrical – Roadside Sign</title>
<link rel="stylesheet" href="https://fonts.googleapis.com/css2?family=Kumbh+Sans:wght@600;700;800&display=swap">
<style>
  :root {
    --sign-black: #000000;
    --page-white: #ffffff;
    --brand-green: #a6ce39;
    --text-white: #ffffff;
  }
  * { margin: 0; padding: 0; box-sizing: border-box; }
  html, body {
    width: 1200px;
    height: 1200px;
    overflow: hidden;
    background: var(--page-white);
    font-family: "Kumbh Sans", sans-serif;
  }
  .sheet { position: relative; width: 1200px; height: 1200px; }
  .panel { position: absolute; background: var(--sign-black); color: var(--text-white); }

  .panel--main { left: 0; top: 0; width: 781px; height: 602px; }
  .panel--freecall { left: 788px; top: 139px; width: 395px; height: 326px; }
  .panel--banner { left: 0; top: 614px; width: 1200px; height: 478px; }
  .panel--phone-strip { left: 0; top: 1108px; width: 602px; height: 92px; }
  .panel--web-strip { left: 618px; top: 1108px; width: 582px; height: 92px; }

  .brand-name {
    position: absolute;
    color: var(--brand-green);
    font-weight: 800;
    line-height: 0.95;
    text-align: center;
    text-transform: uppercase;
    letter-spacing: 0.02em;
  }
  .brand-name span { display: block; }
  .brand-name .brand-name__line2 { font-size: 0.56em; letter-spacing: 0.08em; }

  .panel--main .brand-name { left: 111px; top: 172px; width: 560px; font-size: 98px; }
  .panel--banner .brand-name { left: 140px; top: 60px; width: 900px; font-size: 150px; }

  .services {
    position: absolute;
    font-weight: 600;
    white-space: nowrap;
    letter-spacing: 0.01em;
  }
  .panel--main .services { left: 158px; top: 378px; font-size: 30px; }
  .panel--banner .services { left: 0; width: 1200px; text-align: center; top: 340px; font-size: 33px; }

  .web {
    position: absolute;
    display: flex;
    align-items: center;
    font-weight: 700;
    letter-spacing: 0.04em;
    white-space: nowrap;
  }
  .web svg { flex: none; }
  .panel--main .web { left: 158px; top: 507px; font-size: 32px; gap: 20px; }
  .panel--web-strip .web { left: 78px; top: 24px; font-size: 34px; gap: 26px; }

  .freecall-block {
    position: absolute;
    left: 78px;
    top: 118px;
    font-size: 33px;
    font-weight: 700;
    line-height: 1.45;
    letter-spacing: 0.01em;
  }

  .phone-line {
    position: absolute;
    left: 88px;
    top: 26px;
    font-size: 36px;
    font-weight: 700;
    white-space: nowrap;
    letter-spacing: 0.01em;
  }
  .phone-line .phone-line__number { margin-left: 38px; }
</style>
</head>
<body>
<main class="sheet">

  <section class="panel panel--main">
    <h1 class="brand-name"><span>Briskway</span><span class="brand-name__line2">Electrical</span></h1>
    <p class="services">Design | Installation | Maintenance</p>
    <p class="web">
      <svg width="34" height="34" viewBox="0 0 34 34" aria-hidden="true" fill="none" stroke="#fff" stroke-width="2">
        <circle cx="17" cy="17" r="15"/>
        <ellipse cx="17" cy="17" rx="6.5" ry="15"/>
        <line x1="17" y1="2" x2="17" y2="32"/>
        <line x1="2" y1="17" x2="32" y2="17"/>
        <path d="M5 9.5h24M5 24.5h24"/>
      </svg>
      www.briskway.net.nz
    </p>
  </section>

  <aside class="panel panel--freecall">
    <p class="freecall-block">Freecall<br>0800 342 958</p>
  </aside>

  <section class="panel panel--banner">
    <h2 class="brand-name"><span>Briskway</span><span class="brand-name__line2">Electrical</span></h2>
    <p class="services">Design | Installation | Maintenance</p>
  </section>

  <div class="panel panel--phone-strip">
    <p class="phone-line">Freecall<span class="phone-line__number">0800 342 958</span></p>
  </div>

  <div class="panel panel--web-strip">
    <p class="web">
      <svg width="42" height="42" viewBox="0 0 34 34" aria-hidden="true" fill="none" stroke="#fff" stroke-width="2">
        <circle cx="17" cy="17" r="15"/>
        <ellipse cx="17" cy="17" rx="6.5" ry="15"/>
        <line x1="17" y1="2" x2="17" y2="32"/>
        <line x1="2" y1="17" x2="32" y2="17"/>
        <path d="M5 9.5h24M5 24.5h24"/>
      </svg>
      www.briskway.net.nz
    </p>
  </div>

</main>
</body>
</html>
```